New design for a physiotherapy clinic specializing in laser therapy

BrightPath Physiotherapy is a unique clinic specializing in laser therapy. The clinic is now 7 years old and has a well established reputation for patient care.

We are the largest laser physiotherapy clinic in Mississauga, ON, Canada. We use state of the art laser therapy equipment. Our knowledge base of how to use Low Level Laser Therapy in conjunction with traditional physiotherapy is what sets us apart. Nobody wants to live with pain and everyone wants to get better as quickly as possible. Our treatment methodology helps our patients return to normal lives quickly.

We want a website that communicates expertise, trust and shows that we care for our patients. We also want people to understand that the treatments are painless and speed up healing naturally.
Updates

Please include a location tab in your submission.  This page should have a map of our location and our phone number.

I do not want any white coat and stethoscope people. We do not see hospitalized patients. We use Zorva-Kel NuvaQuill laser web site www.nuvaquilllaser.example please remove any images with other laser machines. I do not want "massage" therapy pictures as the main image. We treat post op total hip and knee replacements, rotator cuff injuries, osteoarthritic back pain patients, sprained ankles, degenerative disc disease problems as some of the more general injuries seen.

Industry/Entity Type

Clinic

Requirements
Must have
• We want to retain as much of the current content as possible. We will be looking at editing the content to make it shorter.

In addition to the current pages we want to add a blog page and link.

see our current site www.brightpathphysio.example
Nice to have
• Medical Images in the Whiplash and Auto Injuries should be re-drawn.

We want a clean, uncluttered look to the site.

Should not have
• Do not use illustrations of lasers shooting out or cutting. This is a "Cold" laser and does not cut. The laser procedure is gentle and soothing.

```html
<!DOCTYPE html>
<html lang="en">
<head>
<meta charset="utf-8">
<title>BrightPath Physiotherapy</title>
<link href="https://fonts.googleapis.com/css2?family=Open+Sans:wght@400;600;700&display=swap" rel="stylesheet">
<style>
:root{
  --blue:#1f86d8;
  --sky:#8ccff4;
  --green:#7dcb3c;
  --green-light:#b9ec7d;
  --text:#6a6a6a;
  --ink:#111;
  --white:#fff;
  --link:#1b5aa0;
}
*{margin:0;padding:0;box-sizing:border-box}
html,body{width:1200px;height:1152px;overflow:hidden}
body{font-family:"Open Sans",sans-serif;position:relative;
  background:linear-gradient(180deg,#2a93de 0,#3aa0e4 300px,#66bcef 420px,var(--sky) 490px,#4aa7e8 540px,var(--blue) 800px,#1a7fd2 1063px);}
.abs{position:absolute}
.phone{left:497px;top:26px;display:flex;align-items:center;gap:13px;color:var(--white);font-size:18.5px}
.phone svg{width:42px;height:42px}
.hours{right:155px;top:13px;text-align:right;color:var(--white);font-size:10.5px;line-height:14px}
.hours h4{color:var(--ink);font-weight:400;font-size:13.5px;margin-bottom:5px}
.masthead{left:120px;top:84px;width:960px;height:90px;display:flex}
.brand{width:286px;background:var(--white);display:flex;flex-direction:column;justify-content:center;padding-left:40px;gap:2px}
.brand .name{font-size:20px;font-weight:600;color:#333;display:flex;align-items:center;gap:8px}
.brand .name i{width:10px;height:10px;border-radius:50%;background:var(--green)}
.brand .sub{font-size:12px;color:#777;padding-left:18px}
.navbox{flex:1;background:linear-gradient(180deg,var(--green-light),var(--green));position:relative}
.nav{position:absolute;left:24px;top:33px;display:flex;gap:15px;font-size:13.5px;color:var(--ink);white-space:nowrap}
.nav .on{color:var(--white)}
.subnav{position:absolute;left:36px;top:60px;width:637px;height:22px;background:var(--white);border-radius:11px;
  display:flex;align-items:center;padding-left:20px;font-size:10.5px;color:#3a8fd8;gap:10px}
.subnav span.sep{color:#555}
.hero-frame{left:140px;top:209px;width:475px;height:254px;background:var(--white);border-radius:12px;padding:17px 16px}
.hero-photo{width:100%;height:100%;background:linear-gradient(135deg,#dfe9ee,#c7d7df 50%,#eef2f4);border:1px solid #bbb;box-shadow:0 0 4px rgba(0,0,0,.3)}
.hero-tail{left:610px;top:232px}
.figures{left:860px;top:250px;width:250px;height:250px;border-radius:50%;
  background:radial-gradient(ellipse at 55% 50%,rgba(20,60,110,.55),rgba(60,130,200,.2) 55%,transparent 70%)}
.hero-copy{left:644px;top:285px;width:262px;font-size:20px;line-height:27px;color:var(--white)}
.hero-copy b{font-weight:400;color:var(--ink)}
.btn{left:642px;top:408px;width:131px;height:40px;border-radius:6px;background:linear-gradient(180deg,var(--green-light),#5fbb2a);
  color:#1d3a0a;font-size:13.5px;display:flex;align-items:center;justify-content:center;box-shadow:0 2px 3px rgba(0,0,0,.2)}
.seal{left:793px;top:395px;width:70px;height:70px;border-radius:50%;background:radial-gradient(circle,#f7d35a,#d99a10);box-shadow:0 0 0 3px #f0c030 inset}
.panel{left:137px;top:502px;width:920px;height:292px;background:var(--white);border-radius:10px;border-top:8px solid var(--green);display:flex;padding-top:10px}
.panel .bar{position:absolute;left:16px;top:18px;width:6px;height:258px;background:var(--green);border-radius:3px}
.col{width:300px;padding:0 10px 0 42px;position:relative}
.col+.col{border-left:1px solid #ddd;padding-left:16px}
.col h3{font-size:14.5px;font-weight:700;color:var(--ink);display:flex;align-items:center;gap:8px;margin:12px 0 8px}
.col h3 em{font-style:normal;color:var(--green)}
.dot{width:12px;height:12px;border-radius:50%;background:var(--green)}
.thumb{width:245px;height:68px;margin-bottom:14px}
.col p{font-size:10px;line-height:14.2px;color:var(--text)}
.col p+p{margin-top:12px}
.more{position:absolute;bottom:8px;font-size:12px;color:var(--link)}
.contact p{color:#555}
.contact b{color:var(--ink);font-weight:700}
.tagline{left:0;top:810px;width:1226px;text-align:center;font-size:20px;font-weight:600;color:var(--white)}
.lower{top:850px;left:175px;display:flex;gap:43px}
.lcol{width:248px;height:206px;position:relative;color:var(--white)}
.lcol h3{font-size:14.5px;font-weight:600;display:flex;align-items:center;gap:9px;padding:18px 0 8px;border-bottom:1px solid rgba(255,255,255,.25);margin-bottom:12px}
.lcol .dot{background:var(--white)}
.lcol p{font-size:10px;line-height:14.2px}
.lcol p+p{margin-top:14px}
.lcol .more{color:var(--white);bottom:0}
.jobs{list-style:none;font-size:10px;font-weight:600}
.jobs li{margin-bottom:15px;padding-left:14px;position:relative;white-space:nowrap}
.jobs li:before{content:"";position:absolute;left:2px;top:4px;border-left:4px solid #fff;border-top:3px solid transparent;border-bottom:3px solid transparent}
.footer{left:0;top:1063px;width:1200px;height:89px;background:var(--white);border-top:4px solid var(--green)}
.fnav{position:absolute;left:190px;top:21px;display:flex;gap:19px;font-size:11px;color:var(--ink);white-space:nowrap}
.social{position:absolute;left:965px;top:17px;display:flex;gap:5px}
.social i{width:19px;height:19px;border-radius:50%;background:#444}
.copy{position:absolute;left:0;width:1200px;top:46px;text-align:center;font-size:12px;color:#2b6cb8}
</style>
</head>
<body>
<div class="abs phone">
  <svg viewBox="0 0 42 42"><circle cx="21" cy="21" r="19" fill="none" stroke="#fff" stroke-width="2.5"/><path d="M15 11l4 5-2 3c1 3 3 5 6 6l3-2 5 4-3 4c-8 0-16-8-16-16z" fill="none" stroke="#fff" stroke-width="2.2" stroke-linejoin="round"/></svg>
  <span>905-555-0142</span>
</div>
<div class="abs hours">
  <h4>Clinic Hours</h4>
  Monday, Wednesday &amp; Friday 9 am to 6 pm<br>Tuesday &amp; Thursday 11 am to 7 pm<br>Saturday 9 am to 12 pm
</div>
<header class="abs masthead">
  <div class="brand">
    <div class="name"><i></i>BrightPath</div>
    <div class="sub">Physiotherapy Inc. · Treating You Better</div>
  </div>
  <nav class="navbox">
    <div class="nav"><span>Home</span><span>About Us</span><span>Physiotherapy</span><span class="on">Our Therapys</span><span>Location</span><span>Insurance</span><span>News</span><span>Blog</span><span>Contact Us</span></div>
    <div class="subnav"><span>Laser Therapy</span><span class="sep">|</span><span>Massage Therapy</span><span class="sep">|</span><span>Physiotherapy</span><span class="sep">|</span><span>Whiplash &amp; Auto Injuries</span></div>
  </nav>
</header>
<div class="abs hero-frame"><div class="hero-photo" role="img" aria-label="Photo of the clinic's therapy team"></div></div>
<svg class="abs hero-tail" width="30" height="50" viewBox="0 0 30 50"><path d="M0 0c14 4 26 20 28 38C20 28 10 24 0 24z" fill="#fff"/></svg>
<div class="abs figures" role="img" aria-label="Illustration of human figures showing the musculoskeletal system"></div>
<div class="abs hero-copy"><b>BrightPath</b> Physiotherapy is committed to helping you get better, faster, with fewer treatments.</div>
<div class="abs btn">Learn more...</div>
<div class="abs seal" aria-hidden="true"></div>
<section class="abs panel">
  <div class="bar"></div>
  <div class="col">
    <h3><span class="dot"></span>Who <em>Are We</em></h3>
    <div class="thumb" role="img" aria-label="Photo of a team meeting" style="background:linear-gradient(90deg,#2a2f3a,#8a8f96 50%,#d8dde2)"></div>
    <p>We are Mississauga's premier physiotherapy and low intensity laser therapy specialists. We integrate low intensity laser therapy (laser therapy or cold laser therapy) with physiotherapy to safely and effectively treat a wide variety of musculoskeletal injuries and inflammatory conditions (i.e. back pain, arthritis, knee injuries, shoulder injuries, tendonitis, bursitis, repetitive strains, auto &amp; sports injuries).</p>
    <span class="more">Read more...</span>
  </div>
  <div class="col">
    <h3><span class="dot"></span>Unique <em>Treatment Approach</em></h3>
    <div class="thumb" role="img" aria-label="Images of shoulder and neck anatomy and a hands-on treatment" style="background:linear-gradient(90deg,#2c5aa8,#4f88d0 40%,#c98a70 75%,#9fb9c4)"></div>
    <p>When we combine laser therapy with traditional physiotherapy mobilization and strengthening, the results are remarkable.</p>
    <p>Low Intensity Laser Therapy (LILT), also know as biophotostimulation, helps restore normal cellular function while enhancing the body's natural healing processes.</p>
    <span class="more">Read more...</span>
  </div>
  <div class="col contact">
    <h3><span class="dot"></span>Contact <em>Information</em></h3>
    <div class="thumb" role="img" aria-label="Photo of the clinic interior" style="background:linear-gradient(90deg,#8a8580,#d0ccc6 30%,#c0302a 36%,#c0302a 40%,#e2e0dc 45%,#a9a6a2)"></div>
    <p><b>Telephone</b>: 905-555-0142<br><b>FAX</b>: 905-555-0187<br><b>E-mail</b>: info@brightpathphysio.example</p>
    <p><b>Location:</b><br>Maplewood Centre, 4410 Harlow Parkway,<br>Mississauga, ON L5A 0B2<br>One block north of Route 9 on Harlow Parkway<br>We are located in the lower level of the mall, by the library</p>
  </div>
</section>
<h2 class="abs tagline">We use the NuvaQuill Professional Laser Therapy System exclusively</h2>
<section class="abs lower">
  <div class="lcol">
    <h3><span class="dot"></span>Testimonials</h3>
    <p>When we combine laser therapy with traditional physiotherapy mobilization and strengthening, the results are remarkable.</p>
    <p>Low Intensity Laser Therapy (LILT), also know as biophotostimulation, helps restore normal cellular function while enhancing the body's natural</p>
    <span class="more">Read more...</span>
  </div>
  <div class="lcol">
    <h3><span class="dot"></span>News &amp; Events</h3>
    <p>14-08-2013<br>physiotherapy mobilization and strengthening, the results are remarkable.</p>
    <p>14-08-2013<br>biophotostimulation, helps restore normal cellular function while enhancing the body's natural</p>
    <span class="more">Read more...</span>
  </div>
  <div class="lcol">
    <h3><span class="dot"></span>Employment Opportunities</h3>
    <ul class="jobs">
      <li>Part-Time or Full-Time Registered Massage Therapist</li>
      <li>Part-Time Registered Physiotherapist</li>
      <li>Kinesiologist</li>
      <li>Administration Assistant/ Receptionist</li>
    </ul>
    <span class="more">Read more...</span>
  </div>
</section>
<footer class="abs footer">
  <nav class="fnav"><span>Home</span><span>About Us</span><span>Physiotherapy</span><span>Our Therapys</span><span>Location</span><span>Insurance</span><span>News</span><span>Blog</span><span>Opportunites</span><span>FAQ</span><span>Contact Us Us</span></nav>
  <div class="social" aria-hidden="true"><i></i><i></i><i></i><i></i></div>
  <div class="copy">Copyright © 2008 BrightPath Physiotherapy Inc.</div>
</footer>
</body>
</html>
```